I need a great, modern, professional website for my paint contracting company, Brookhollow Paint Contractors, LLC. I have many good pix that can be used from jobs completed that would be attractive. We do commercial, residential and industrial jobs. I’m fully insured and licensed, including holding a General Contractor’s License as a Subcontractor. I know nothing about coding websites. I’ll have my assistant get on tomorrow and learn how to drop files. I’m not sure what files to send. This will be difficult at best, it being able to talk this through. Oh well. What’s next?

Target Market(s)

General Contractors

Industry/Entity Type

Paint Contracting

Coding

Coded - Design and coding required

Font styles to use
Sans Serif

Colors
00AB8E
00BBA5
67D7C9
C6EFE9
E9F9F6

Requirements
Must have
• Pix of completed jobs, bio, maybe testimonials from happy customers? ….
Nice to have
• I’d like it to have a modern appeal, but still have some warmth.
Should not have
• ??

```html
<!DOCTYPE html>
<html lang="en">
<head>
<meta charset="utf-8">
<title>Brookhollow Paint Contractors, LLC</title>
<link rel="stylesheet" href="https://fonts.googleapis.com/css2?family=Poppins:wght@400;500;600&family=Roboto:wght@500;700&display=swap">
<style>
:root{
  --teal:#00AB8E;
  --teal-2:#00BBA5;
  --teal-3:#67D7C9;
  --teal-4:#C6EFE9;
  --teal-5:#E9F9F6;
  --ink:#1f2326;
  --text:#333;
  --muted:#8a8f93;
  --grey-bg:#f3f5f4;
  --white:#fff;
}
*{margin:0;padding:0;box-sizing:border-box}
html,body{width:1200px;height:5217px;overflow:hidden}
body{font-family:"Poppins",sans-serif;color:var(--text);background:var(--white)}
section,header,footer{position:relative;width:1200px;overflow:hidden}
.abs{position:absolute}
.h-sub{font-family:"Poppins",sans-serif;font-size:24px;color:var(--ink)}
.h-main{font-family:"Roboto",sans-serif;font-weight:700;font-size:37px;color:var(--ink);text-transform:uppercase;letter-spacing:.3px}
.center{left:0;width:1200px;text-align:center}
.btn{display:inline-block;background:var(--teal);color:#fff;font-weight:600;font-size:17px;text-transform:uppercase;border-radius:32px;text-align:center}
.body-copy{font-size:15px;line-height:28px;color:var(--muted)}

/* header */
.site-header{height:110px}
.brand-mark{left:110px;top:48px;width:14px;height:14px;background:var(--teal)}
.brand-name{left:134px;top:42px;font-family:"Poppins",sans-serif;font-weight:600;font-size:16px;color:var(--ink);white-space:nowrap}
.nav{left:482px;top:44px;display:flex;gap:18px;font-size:15px;font-weight:500;color:var(--ink)}
.nav .active{color:var(--teal)}
.call{left:914px;top:18px}
.call-text{left:962px;top:18px;font-size:14px;line-height:20px;color:var(--ink)}
.call-num{left:960px;top:62px;font-family:"Roboto",sans-serif;font-weight:700;font-size:21px;color:var(--teal);letter-spacing:1px}

/* hero */
.hero{height:657px}
.hero-photo{width:1200px;height:657px;background:linear-gradient(180deg,#2f82c6 0%,#7cb9e4 35%,#c88a5c 62%,#6b4030 82%,#2a241f 100%)}
.hero-title{left:110px;top:68px;font-family:"Roboto",sans-serif;font-weight:700;font-size:58px;line-height:66px;color:#fff;text-transform:uppercase}
.hero-text{left:110px;top:214px;font-size:18px;line-height:26px;color:#fff}
.hero .btn{left:110px;top:292px;width:262px;height:64px;line-height:64px}

/* welcome */
.welcome{height:393px}
.welcome .h-sub{left:110px;top:68px}
.welcome .h-main{left:110px;top:106px;line-height:48px;font-size:37px}
.video{left:110px;top:228px;display:flex;align-items:center;gap:20px;font-size:17px;color:var(--ink)}
.welcome .body-copy{left:505px;top:58px;width:555px}
.welcome .btn{left:505px;top:254px;width:156px;height:60px;line-height:60px}

/* services */
.services{height:890px;background:var(--grey-bg)}
.services .h-sub{top:68px}
.services .h-main{top:108px}
.svc{top:200px;width:300px;text-align:center;font-family:"Roboto",sans-serif;font-weight:500;font-size:23px;color:var(--ink)}
.svc svg{display:block;margin:0 auto 22px}
.svc-card{left:110px;top:435px;width:978px;height:360px;background:#fff;box-shadow:0 2px 12px rgba(0,0,0,.06)}
.svc-photo{left:0;top:0;width:473px;height:360px;background:linear-gradient(135deg,#aebcc9 0%,#5d6466 45%,#3f5a2e 80%,#2c3b22 100%)}
.svc-card h3{left:514px;top:38px;font-family:"Roboto",sans-serif;font-weight:500;font-size:27px;color:var(--ink)}
.svc-card .body-copy{left:514px;top:86px;width:400px}
.svc-card .btn{left:514px;top:262px;width:262px;height:58px;line-height:58px}

/* benefits */
.benefits{height:560px;background:linear-gradient(90deg,var(--teal-4) 0%,var(--teal-5) 55%,#f4f6f6 100%)}
.benefit-photo{left:560px;top:0;width:640px;height:560px;background:linear-gradient(110deg,rgba(233,249,246,0) 0%,#eef0f0 25%,#dfe3e4 55%,#3a8fc4 78%,#2a6f9e 100%)}
.benefits .h-sub{left:110px;top:72px}
.benefits .h-main{left:110px;top:110px}
.benefits .body-copy{left:110px;top:174px;width:400px;font-size:14px;line-height:26px}
.benefit{display:flex;align-items:center;gap:14px;font-size:17px;color:var(--ink)}
.badge{width:98px;height:98px;border-radius:50%;background:#fff;box-shadow:0 3px 10px rgba(0,0,0,.12);display:flex;align-items:center;justify-content:center}

/* portfolio */
.portfolio{height:1070px}
.portfolio .h-sub{top:88px}
.portfolio .h-main{top:126px}
.tabs{left:0;width:1200px;top:178px;display:flex;justify-content:center;gap:36px;font-size:17px;color:var(--ink)}
.tabs span{padding:4px 10px}
.tabs .on{background:var(--teal);color:#fff;border-radius:4px}
.tile{width:314px;height:306px}
.portfolio .btn{left:522px;top:942px;width:156px;height:58px;line-height:58px}

/* testimonials */
.testimonials{height:540px;background:var(--grey-bg)}
.testimonials .h-sub{top:74px}
.testimonials .h-main{top:112px}
.review{background:#fff;text-align:center}
.stars{font-size:20px;letter-spacing:3px;color:var(--ink)}
.quote{font-style:italic;font-size:14px;line-height:25px;color:var(--text);margin-top:14px}
.who{font-weight:600;font-size:16px;color:var(--ink);margin-top:18px}
.where{font-size:15px;color:var(--ink)}

/* contact */
.contact{height:575px;background:var(--teal)}
.contact-photo{left:0;top:0;width:447px;height:575px;background:linear-gradient(180deg,#5b7bb0 0%,#8aa0c2 30%,#8f5a5a 55%,#3e3a34 80%,#2b2f30 100%)}
.contact .h-sub{left:513px;top:56px;color:#fff}
.contact .h-main{left:513px;top:92px;color:#fff}
.field{background:#fff;border:1px solid #d9d9d9;font-size:14px;color:#555;padding:14px 18px}
.submit{left:522px;top:456px;width:130px;height:56px;line-height:56px;background:#252525;color:#fff;border-radius:30px;text-align:center;font-weight:600;font-size:16px}

/* footer */
.site-footer{height:422px}
.f-mark{left:110px;top:104px;width:18px;height:18px;background:var(--teal)}
.f-brand{left:140px;top:92px;font-family:"Poppins",sans-serif;font-weight:600;font-size:24px;line-height:36px;color:var(--ink)}
.f-head{font-weight:600;font-size:16px;color:var(--ink)}
.f-links{left:467px;top:74px;font-size:15px;line-height:29px;color:var(--text)}
.f-contact{left:655px;top:74px;font-size:15px;line-height:26px;color:var(--text)}
.f-line{left:110px;top:326px;width:978px;height:1px;background:#ccc}
.copy{left:110px;top:372px;font-size:14px;color:var(--text)}
.social{top:358px;width:46px;height:46px;border:2px solid var(--teal);border-radius:50%}
</style>
</head>
<body>

<header class="site-header">
  <div class="abs brand-mark"></div>
  <div class="abs brand-name">Brookhollow Paint Contractors, LLC</div>
  <nav class="abs nav"><span class="active">Home</span><span>About</span><span>Services</span><span>Portfolio</span><span>Reviews</span><span>Contact</span></nav>
  <svg class="abs call" width="40" height="40" viewBox="0 0 40 40"><circle cx="20" cy="20" r="18.5" fill="none" stroke="#333" stroke-width="1.5"/><path d="M14 12c1-1 2-1 3 0l2 3c.5 1 0 2-1 2.5 1 2 3 4 5 5 .5-1 1.5-1.5 2.5-1l3 2c1 1 1 2 0 3-2 2-5 1.5-9-2.5s-4.5-7-2.5-9z" fill="none" stroke="#00AB8E" stroke-width="1.5"/></svg>
  <div class="abs call-text">Call today for a<br>free estimate</div>
  <div class="abs call-num">1 555 010 2040</div>
</header>

<section class="hero">
  <div class="abs hero-photo" role="img" aria-label="Photo of a brightly painted multi-storey riverside building at dusk"></div>
  <h1 class="abs hero-title">Brookhollow<br>Paint Contractor</h1>
  <p class="abs hero-text">Fully insured and licensed, including holding a General<br>Contractor's License as a Subcontractor</p>
  <a class="abs btn">Request an estimate</a>
</section>

<section class="welcome">
  <div class="abs h-sub">Welcome to</div>
  <h2 class="abs h-main">Brookhollow Paint<br>Contractors</h2>
  <div class="abs video">
    <svg width="58" height="58" viewBox="0 0 58 58"><circle cx="29" cy="29" r="27.5" fill="none" stroke="#333" stroke-width="1.5"/><path d="M23 18l16 11-16 11z" fill="#00AB8E"/></svg>
    Watch Our Video
  </div>
  <p class="abs body-copy">Nemo enim ipsam voluptatem quia voluptas sit aspernatur aut odit aut fugit, sed quia consequuntur magni dolores eos qui ratione voluptatem sequi nesciunt. Neque porro quisquam est, qui dolorem ipsum quia dolor sit amet, consectetur, adipisci velit, sed quia non numquam eius modi tempora incidunt ut labore et dolore magnam aliquam quaerat voluptatem.</p>
  <a class="abs btn">Read more</a>
</section>

<section class="services">
  <div class="abs h-sub center">Our</div>
  <h2 class="abs h-main center">Service Area</h2>
  <div class="abs svc" style="left:104px">
    <svg width="104" height="104" viewBox="0 0 104 104" fill="none" stroke="#222" stroke-width="3"><path d="M10 100V8l50 14v78M60 50h36v50M4 100h96"/><path d="M22 34h4M34 34h4M46 34h4M22 50h4M34 50h4M46 50h4M22 66h4M34 66h4M46 66h4M22 82h4M34 82h4M46 82h4" stroke-width="4"/></svg>
    Commercial Painting
  </div>
  <div class="abs svc" style="left:450px">
    <svg width="104" height="104" viewBox="0 0 104 104" fill="none" stroke="#00AB8E" stroke-width="3"><path d="M6 60L52 18l46 42M16 52v48h72V52M36 30V10h32v20M44 100V80h16v20M34 66h36"/><path d="M46 40h4M54 40h4M30 58h4M40 58h4M60 58h4M70 58h4" stroke-width="4"/></svg>
    Residential Painting
  </div>
  <div class="abs svc" style="left:796px">
    <svg width="118" height="104" viewBox="0 0 118 104" fill="none" stroke="#222" stroke-width="3"><path d="M4 100V60l20-12v12l20-12v12l20-12v12l20-12V6h16v94zM4 100h108M84 20h16"/><path d="M20 80h4M32 80h4M44 80h4M56 80h4M68 80h4M80 80h4M20 90h4M32 90h4M44 90h4M56 90h4M68 90h4M80 90h4" stroke-width="4"/></svg>
    Industrial Painting
  </div>
  <div class="abs svc-card">
    <div class="abs svc-photo" role="img" aria-label="Photo of a painter on a ladder painting a grey house siding"></div>
    <h3 class="abs">Residential Painting</h3>
    <p class="abs body-copy">Neque porro quisquam est, qui dolorem ipsum quia dolor sit amet, consectetur, adipisci velit, sed quia non numquam eius modi tempora incidunt ut labore et dolore magnam aliquam quaerat voluptatem.</p>
    <a class="abs btn">Request an estimate</a>
  </div>
</section>

<section class="benefits">
  <div class="abs benefit-photo" role="img" aria-label="Photo of a painter in a cap using a roller on a white wall"></div>
  <div class="abs h-sub">Benefits</div>
  <h2 class="abs h-main">Why Choose Us</h2>
  <p class="abs body-copy">Nemo enim ipsam voluptatem quia voluptas sit aspernatur aut odit aut fugit, sed .</p>
  <div class="abs benefit" style="left:104px;top:250px"><div class="badge"><svg width="46" height="46" viewBox="0 0 46 46" fill="none" stroke="#222" stroke-width="2.5"><path d="M23 4l16 6v12c0 10-7 17-16 20-9-3-16-10-16-20V10z"/><path d="M15 23l6 6 10-11"/></svg></div>Insured</div>
  <div class="abs benefit" style="left:318px;top:250px"><div class="badge"><svg width="46" height="46" viewBox="0 0 46 46" fill="none" stroke="#222" stroke-width="2.5"><circle cx="23" cy="18" r="13"/><circle cx="23" cy="18" r="7"/><path d="M15 29l-4 14 6-3 4 5 2-13M31 29l4 14-6-3-4 5"/></svg></div>Licensed</div>
  <div class="abs benefit" style="left:104px;top:374px"><div class="badge"><svg width="46" height="46" viewBox="0 0 46 46" fill="none" stroke="#222" stroke-width="2.5"><path d="M4 20h8v22H4zM12 24l10-12c2-3 6-1 5 3l-2 7h12c3 0 4 3 3 5l-4 12c-1 2-2 3-4 3H12"/><path d="M30 4l3 5 5-6" stroke="#00AB8E"/></svg></div>Trusted</div>
  <div class="abs benefit" style="left:318px;top:374px"><div class="badge"><svg width="46" height="46" viewBox="0 0 46 46" fill="none" stroke="#222" stroke-width="2.5"><circle cx="20" cy="14" r="9"/><path d="M4 42c0-10 7-16 16-16 4 0 7 1 9 3"/><path d="M34 28l3 6 6 1-5 4 1 6-5-3-5 3 1-6-5-4 6-1z" stroke-width="2"/></svg></div>Experienced</div>
</section>

<section class="portfolio">
  <div class="abs h-sub center">Portfolio</div>
  <h2 class="abs h-main center">Our Work - Brookhollow</h2>
  <div class="abs tabs"><span class="on">All</span><span>Residential</span><span>Commercial</span><span>Industrial</span></div>
  <div class="abs tile" style="left:110px;top:252px;background:linear-gradient(180deg,#9cc3e6 0%,#c9d7e3 40%,#5c6166 70%,#808080 100%)" role="img" aria-label="Photo of a freshly painted grey commercial building"></div>
  <div class="abs tile" style="left:443px;top:252px;background:linear-gradient(180deg,#8fa9c9 0%,#e0d6cc 40%,#3a4a5a 60%,#7f94ab 100%)" role="img" aria-label="Photo of waterfront houses reflected in a harbour"></div>
  <div class="abs tile" style="left:776px;top:252px;background:linear-gradient(180deg,#2f3b40 0%,#46545a 45%,#b9bec0 75%,#e5e6e6 100%)" role="img" aria-label="Photo of an office with a dark accent wall and desks"></div>
  <div class="abs tile" style="left:110px;top:576px;background:linear-gradient(180deg,#e9e9e9 0%,#d4d4d4 45%,#9e8572 80%,#8b7362 100%)" role="img" aria-label="Photo of an empty office with wooden floors"></div>
  <div class="abs tile" style="left:443px;top:576px;background:linear-gradient(180deg,#f2f2f0 0%,#e7e5e0 50%,#6f9c9e 75%,#b79d7c 100%)" role="img" aria-label="Photo of a white living room with a teal sofa and staircase"></div>
  <div class="abs tile" style="left:776px;top:576px;background:linear-gradient(180deg,#f4f5f5 0%,#e3e6e8 50%,#c9ccd0 80%,#dcdcdc 100%)" role="img" aria-label="Photo of a large bright open-plan office floor"></div>
  <a class="abs btn">View more</a>
</section>

<section class="testimonials">
  <div class="abs h-sub center">Testimonials</div>
  <h2 class="abs h-main center">Customer Reviews</h2>
  <div class="abs review" style="left:110px;top:210px;width:326px;height:230px;padding:34px 22px">
    <div class="stars">★★★★★</div>
    <p class="quote">" Nemo enim ipsam voluptatem quia voluptas sit aspernatur aut odit aut fugit, sed quisera conse quuntur magni doloresi "</p>
    <div class="who">Marla</div><div class="where">Brookhollow,sc</div>
  </div>
  <div class="abs review" style="left:420px;top:186px;width:360px;height:276px;padding:40px 30px;box-shadow:0 4px 16px rgba(0,0,0,.08);z-index:2">
    <div class="stars">★★★★★</div>
    <p class="quote" style="font-size:16px;line-height:27px">" Nemo enim ipsam voluptatem quisera voluptas sit aspernatur aut odit aut fgtyugit, sed quisera conse quuntur magni doloresi "</p>
    <div class="who">Marla</div><div class="where">Brookhollow,sc</div>
  </div>
  <div class="abs review" style="left:764px;top:210px;width:326px;height:230px;padding:34px 22px">
    <div class="stars">★★★★★</div>
    <p class="quote">" Nemo enim ipsam voluptatem quia voluptas sit aspernatur aut odit aut fugit, sed quisera conse quuntur magni doloresi "</p>
    <div class="who">Marla</div><div class="where">Brookhollow,sc</div>
  </div>
</section>

<section class="contact">
  <div class="abs contact-photo" role="img" aria-label="Photo of a riverside town with a waterfall at dusk"></div>
  <div class="abs h-sub">Request an Appointment</div>
  <h2 class="abs h-main">Contact Us</h2>
  <div class="abs field" style="left:514px;top:168px;width:280px;height:52px">First Name *</div>
  <div class="abs field" style="left:808px;top:168px;width:280px;height:52px">Last Name *</div>
  <div class="abs field" style="left:514px;top:234px;width:280px;height:52px">Email *</div>
  <div class="abs field" style="left:808px;top:234px;width:280px;height:52px">Phone *</div>
  <div class="abs field" style="left:514px;top:300px;width:574px;height:122px">Message *</div>
  <div class="abs submit">SUBMIT</div>
</section>

<footer class="site-footer">
  <div class="abs f-mark"></div>
  <div class="abs f-brand">Brookhollow Paint<br>Contractors, LLC</div>
  <div class="abs f-links"><div class="f-head" style="margin-bottom:8px">Quick Links</div>Home<br>About<br>Services<br>Portfolio<br>Reviews<br>Contact</div>
  <div class="abs f-contact">
    <div class="f-head" style="margin-bottom:8px">Contact Us</div>
    Brookhollow Paint Contractors, LLC<br>
    <svg width="12" height="14" viewBox="0 0 12 14"><path d="M6 0a5 5 0 015 5c0 4-5 9-5 9S1 9 1 5a5 5 0 015-5z" fill="#00AB8E"/><circle cx="6" cy="5" r="2" fill="#fff"/></svg> 48 Lantern Ridge Way<br>
    <span style="padding-left:18px">Brookhollow, SC 29601</span><br><br>
    <svg width="14" height="14" viewBox="0 0 14 14"><path d="M3 1l2 3-1.5 1.5c1 2 3 4 5 5L10 9l3 2-1 2c-5 0-11-6-11-11z" fill="#00AB8E"/></svg> 1 555 010 2040<br><br>
    <svg width="14" height="12" viewBox="0 0 14 12"><rect x="0" y="0" width="14" height="12" rx="1" fill="#00AB8E"/><path d="M1 1l6 5 6-5" stroke="#fff" fill="none"/></svg> info@brookhollowpaint.com
  </div>
  <div class="abs f-line"></div>
  <div class="abs copy">© Brookhollow Paint Contractors, LLC, 2023. All Rights Reserved.</div>
  <div class="abs social" style="left:926px"></div>
  <div class="abs social" style="left:984px"></div>
  <div class="abs social" style="left:1042px"></div>
</footer>

</body>
</html>
```